Willowmere Equine Sanctuary Flyer Urgent

Willowmere Equine Sanctuary

Rescue • Rehabilitation • Sanctuary

Willowmere Equine Sanctuary provides a safe and ethical refuge for horses, ponies and donkeys who have nowhere else to go. Some arrive needing rehabilitation and careful retraining, while others find permanent sanctuary here due to age, injury or behavioural needs.

Our mission is simple: to improve the physical and psychological wellbeing of every animal in our care.

At Willowmere we focus on:
• Rescue and rehabilitation of horses in need
• Lifetime sanctuary for those who cannot be rehomed
• Education and advocacy for responsible horse care
• Equine rehabilitation services to help horses recover and thrive

Sponsor a Horse

One of the most meaningful ways to support our work is by sponsoring one of our residents. Each horse, pony or donkey only has one sponsor!

Your sponsorship helps provide:
• Hay and feed
• Veterinary care
• Hoof trimming and routine health care
• Rugs, shelter and daily care

Many of our horses will live out their lives here, and sponsorship ensures they are safe, well fed and cared for every single day.

Sponsorship starts from $15 - $25 per week / $60 -$100 per month.

How You Can Help

• Sponsor a horse
• Make a donation
• Share our work with others

Your support helps us continue to say yes to horses who need a second chance.

📍 Willowmere Park, Victoria
📧 clara@willowmerepark-example.org

📞 0400 519 627

Font styles to use
Serif
Sans Serif

Colors
F0912C
F2A743
F7CA91
FBE8D2
FDF5EE
EE7325
F08F49
F5BC92
FAE3D3
FDF4ED

Requirements
Should not have
• Photos not provided by Willowmere

```html
<!DOCTYPE html>
<html lang="en">
<head>
<meta charset="utf-8">
<title>Willowmere Equine Sanctuary – Sponsorship Flyer</title>
<link rel="stylesheet" href="https://fonts.googleapis.com/css2?family=Cinzel:wght@400;600;700&family=Crimson+Pro:wght@400;600;700&display=swap">
<style>
  :root{
    --backdrop:#4a4a4a;
    --paper:#ffffff;
    --orange:#e47b06;
    --orange-soft:#f28c2c;
    --ink:#1c1c1c;
    --night:#111111;
    --blue:#1414f0;
    --mist:#e9e9ea;
    --white:#ffffff;
  }
  *{box-sizing:border-box;margin:0;padding:0}
  html,body{width:1200px;height:1200px;overflow:hidden;background:var(--backdrop)}
  body{position:relative;font-family:"Crimson Pro",Georgia,serif;color:var(--ink)}
  h1,h2{font-weight:400}
  .flyer{position:absolute;left:228px;top:73px;width:744px;height:1052px;background:var(--paper);overflow:hidden}

  .hero{position:absolute;left:0;top:0;width:553px;height:432px;background:var(--orange);color:var(--white)}
  .brand{position:absolute;left:27px;top:52px;display:flex;align-items:center;gap:8px;font-family:"Cinzel",serif;font-weight:400;font-size:19px;line-height:1;letter-spacing:.5px}
  .brand-square{width:14px;height:14px;background:var(--white)}
  .hero-title{position:absolute;left:27px;top:170px;width:310px;font-family:"Cinzel",serif;font-weight:600;font-size:40px;line-height:52px;letter-spacing:.3px}
  .hero-tagline{position:absolute;left:27px;top:375px;font-family:"Cinzel",serif;font-size:13.5px;letter-spacing:.6px}
  .hero-tagline span{font-size:8px;vertical-align:middle;margin:0 6px}

  .hero-frame{position:absolute;left:345px;top:35px;width:327px;height:358px;background:var(--white)}
  .hero-photo{position:absolute;left:353px;top:43px;width:311px;height:342px;background:linear-gradient(135deg,#5d6a3f 0%,#b05a22 40%,#c7692b 60%,#6f7a4a 100%)}

  .intro{position:absolute;left:27px;top:455px;width:370px;padding-left:16px;border-left:2px solid var(--orange);font-size:14.3px;line-height:18px}

  .sponsor-card{position:absolute;left:27px;top:567px;width:365px;height:194px;background:linear-gradient(90deg,#3b3b3d 55%,#1a1a1a 100%)}
  .sponsor-photo{position:absolute;left:0;top:0;width:214px;height:194px;background:linear-gradient(160deg,#8fa1b8 0%,#6d4a33 45%,#3a2518 100%)}
  .sponsor-head{position:absolute;left:225px;top:10px;font-family:"Cinzel",serif;font-weight:400;color:var(--white);font-size:26px;line-height:30px}
  .sponsor-head .hl{display:inline-block;background:var(--orange);padding:0 8px 0 4px;font-weight:600;font-size:29px;margin-right:-10px}
  .sponsor-text{position:absolute;left:225px;top:92px;width:136px;color:var(--white);font-size:11px;line-height:15px}

  .mission{position:absolute;left:430px;top:455px;width:283px;height:308px;background:linear-gradient(160deg,#1f1f1f,#0c0c0c);color:var(--white);padding:14px 13px}
  .mission-lead{font-weight:700;color:var(--orange);font-size:13.5px;letter-spacing:.4px;text-transform:uppercase}
  .mission-body{font-size:14px;line-height:18px}
  .mission-sub{color:var(--orange);font-size:14px;margin-top:14px;display:inline-block;border-bottom:1px solid var(--orange);padding-bottom:1px}
  .focus-list{list-style:none;margin-top:8px}
  .focus-list li{position:relative;padding:6px 0 6px 28px;font-size:14px;line-height:18px;border-bottom:1px dotted #777}
  .focus-list li:last-child{border-bottom:none}
  .tick{position:absolute;left:0;top:8px;width:13px;height:13px}

  .helps-band{position:absolute;left:0;top:768px;width:325px;height:26px;background:var(--blue);color:var(--white);font-family:"Cinzel",serif;font-weight:400;font-size:14px;line-height:26px;padding-left:28px;white-space:nowrap}
  .helps-list{position:absolute;left:27px;top:803px;width:370px;display:grid;grid-template-columns:140px 1fr;row-gap:6px;list-style:none}
  .helps-list li{position:relative;padding-left:21px;color:var(--blue);font-size:12px;font-weight:600;line-height:16px}
  .helps-list .tick{top:2px;width:12px;height:12px}
  .helps-note{position:absolute;left:27px;top:851px;width:350px;font-size:9.6px;line-height:13.5px}

  .price{position:absolute;left:430px;top:768px;width:283px;height:81px;background:var(--orange-soft);color:var(--white)}
  .price-label{position:absolute;left:7px;top:5px;color:var(--blue);font-family:"Cinzel",serif;font-size:12.5px}
  .price-amounts{position:absolute;left:7px;top:24px;display:flex;align-items:flex-start}
  .price-item{text-align:right;font-weight:700;font-size:25px;line-height:28px}
  .price-item small{display:block;font-size:8px;line-height:8px;font-weight:600}
  .price-divider{width:1px;height:30px;background:var(--white);margin:6px 10px 0}
  .price-mark{position:absolute;right:8px;top:28px;width:18px;height:18px;background:var(--white)}

  .backdrop-herd{position:absolute;left:0;top:800px;width:744px;height:180px;background:linear-gradient(180deg,rgba(233,233,234,0) 0%,var(--mist) 55%,rgba(233,233,234,.5) 100%)}

  .help-title{position:absolute;left:0;width:744px;top:889px;text-align:center;color:var(--blue);font-family:"Cinzel",serif;font-weight:400;font-size:16.5px;letter-spacing:.5px}
  .help-arrow{position:absolute;left:367px;top:910px;width:10px;height:8px}
  .actions{position:absolute;left:88px;top:928px;display:flex;gap:5px}
  .action{height:25px;background:var(--night);color:var(--white);font-weight:600;font-size:11.5px;line-height:25px;text-align:center;letter-spacing:.2px;text-transform:uppercase}

  .footer{position:absolute;left:0;top:977px;width:744px;height:75px;background:#000;color:var(--white)}
  .ribbon-flap{position:absolute;top:964px;width:20px;height:13px;background:#b45d04}
  .ribbon{position:absolute;left:164px;top:964px;width:415px;height:41px;background:var(--orange);border-radius:0 0 8px 8px;color:var(--white);font-family:"Cinzel",serif;font-size:12.5px;line-height:16px;text-align:center;padding-top:5px;letter-spacing:.6px}
  .contact{position:absolute;top:1017px;display:flex;align-items:center;gap:7px;color:var(--white);font-size:13.5px;white-space:nowrap}
  .contact svg{width:14px;height:14px}
</style>
</head>
<body>
<main class="flyer">

  <section class="hero">
    <div class="brand"><span class="brand-square"></span>Willowmere Park</div>
    <h1 class="hero-title">WILLOWMERE<br>EQUINE<br>SANCTUARY</h1>
    <p class="hero-tagline">Rescue<span>•</span>Rehabilitation<span>•</span>Sanctuary</p>
  </section>
  <div class="hero-frame"></div>
  <div class="hero-photo" role="img" aria-label="Photo of two chestnut horses with heads lowered together"></div>

  <p class="intro">Willowmere Equine Sanctuary provides a safe and ethical refuge for horses, ponies and donkeys who have nowhere else to go. Some arrive needing rehabilitation and careful retraining, while others find permanent sanctuary here due to age, injury or behavioural needs.</p>

  <section class="sponsor-card">
    <div class="sponsor-photo" role="img" aria-label="Photo of two bay horses standing close together"></div>
    <h2 class="sponsor-head">SPONSOR<br>A <span class="hl">HORSE</span></h2>
    <p class="sponsor-text">One of the most meaningful ways to support our work is by sponsoring one of our residents.<br>Each horse, pony or donkey only has one sponsor!</p>
  </section>

  <section class="mission">
    <p class="mission-lead">Our mission is simple:</p>
    <p class="mission-body">to improve the physical and psychological wellbeing of every animal in our care.</p>
    <p class="mission-sub">At Willowmere we focus on:</p>
    <ul class="focus-list">
      <li><svg class="tick" viewBox="0 0 14 14"><circle cx="7" cy="7" r="7" fill="#e47b06"/><path d="M3.8 7.2l2.2 2.1 4.2-4.4" stroke="#fff" stroke-width="1.6" fill="none"/></svg>Rescue and rehabilitation of horses in need</li>
      <li><svg class="tick" viewBox="0 0 14 14"><circle cx="7" cy="7" r="7" fill="#e47b06"/><path d="M3.8 7.2l2.2 2.1 4.2-4.4" stroke="#fff" stroke-width="1.6" fill="none"/></svg>Lifetime sanctuary for those who cannot be rehomed</li>
      <li><svg class="tick" viewBox="0 0 14 14"><circle cx="7" cy="7" r="7" fill="#e47b06"/><path d="M3.8 7.2l2.2 2.1 4.2-4.4" stroke="#fff" stroke-width="1.6" fill="none"/></svg>Education and advocacy for responsible horse care</li>
      <li><svg class="tick" viewBox="0 0 14 14"><circle cx="7" cy="7" r="7" fill="#e47b06"/><path d="M3.8 7.2l2.2 2.1 4.2-4.4" stroke="#fff" stroke-width="1.6" fill="none"/></svg>Equine rehabilitation services to help horses recover and thrive</li>
    </ul>
  </section>

  <div class="backdrop-herd" role="img" aria-label="Faint greyscale photo of horses grazing in a paddock"></div>

  <h2 class="helps-band">YOUR SPONSORSHIP HELPS PROVIDE:</h2>
  <ul class="helps-list">
    <li><svg class="tick" viewBox="0 0 14 14"><circle cx="7" cy="7" r="7" fill="#e47b06"/><path d="M3.8 7.2l2.2 2.1 4.2-4.4" stroke="#fff" stroke-width="1.6" fill="none"/></svg>Hay and feed</li>
    <li><svg class="tick" viewBox="0 0 14 14"><circle cx="7" cy="7" r="7" fill="#e47b06"/><path d="M3.8 7.2l2.2 2.1 4.2-4.4" stroke="#fff" stroke-width="1.6" fill="none"/></svg>Hoof trimming and routine health care</li>
    <li><svg class="tick" viewBox="0 0 14 14"><circle cx="7" cy="7" r="7" fill="#e47b06"/><path d="M3.8 7.2l2.2 2.1 4.2-4.4" stroke="#fff" stroke-width="1.6" fill="none"/></svg>Veterinary care</li>
    <li><svg class="tick" viewBox="0 0 14 14"><circle cx="7" cy="7" r="7" fill="#e47b06"/><path d="M3.8 7.2l2.2 2.1 4.2-4.4" stroke="#fff" stroke-width="1.6" fill="none"/></svg>Rugs, shelter and daily care</li>
  </ul>
  <p class="helps-note">Many of our horses will live out their lives here, and sponsorship ensures they are safe, well fed and cared for every single day.</p>

  <section class="price">
    <p class="price-label">SPONSORSHIP STARTS FROM</p>
    <div class="price-amounts">
      <div class="price-item">$15 - $25<small>per week</small></div>
      <div class="price-divider"></div>
      <div class="price-item">$60 - $100<small>per month</small></div>
    </div>
    <span class="price-mark"></span>
  </section>

  <h2 class="help-title">How You Can Help</h2>
  <svg class="help-arrow" viewBox="0 0 10 8"><path d="M0 0h10L5 8z" fill="#e47b06"/></svg>
  <nav class="actions">
    <div class="action" style="width:168px">Sponsor a horse</div>
    <div class="action" style="width:168px">Make a donation</div>
    <div class="action" style="width:220px">Share our work with others</div>
  </nav>

  <footer class="footer"></footer>
  <span class="ribbon-flap" style="left:150px"></span>
  <span class="ribbon-flap" style="left:573px"></span>
  <p class="ribbon">YOUR SUPPORT HELPS US CONTINUE TO SAY YES<br>TO HORSES WHO NEED A SECOND CHANCE.</p>

  <p class="contact" style="left:44px"><svg viewBox="0 0 14 14"><path d="M7 13s4.5-4.6 4.5-7.8A4.5 4.5 0 0 0 2.5 5.2C2.5 8.4 7 13 7 13z" fill="none" stroke="#e47b06" stroke-width="1.2"/><circle cx="7" cy="5.3" r="1.6" fill="none" stroke="#e47b06" stroke-width="1.2"/></svg>Willowmere Park, Victoria</p>
  <p class="contact" style="left:318px"><svg viewBox="0 0 14 14"><path d="M3 1.5l2 2.8-1.2 1.4a7 7 0 0 0 4.5 4.5l1.4-1.2 2.8 2-1.3 1.6C6.5 13 1 7.5 1.4 2.8z" fill="none" stroke="#e47b06" stroke-width="1.1"/></svg>0400 519 627</p>
  <p class="contact" style="left:492px"><svg viewBox="0 0 14 14"><rect x="1" y="3" width="12" height="8.5" fill="none" stroke="#e47b06" stroke-width="1.1"/><path d="M1 3l6 5 6-5" fill="none" stroke="#e47b06" stroke-width="1.1"/></svg>clara@willowmerepark-example.org</p>

</main>
</body>
</html>
```